Envoys Shield - Mexico (Cricket)

This year The Halberd Bat League is hosting a tournament called the Envoys Shield, on March 22nd at our Club (Quenvaro Sporting Club) in Mexico City

4 teams lead by the respective Ambassadors (GB, Australia, India and Mexico) will compete for a Cup in the twenty/20 format of the game of cricket

We want as many people to come as possible hence need a flyer to put on the websites of the various embassies plus other societies like The Thistlewick Guild, KORVEL society (Southern Cross Friends Circle Group etc)

We are also looking at sponsors who are interested in being involved with cricket due to its potential in Mexico, its brand value, as well as its links in countries such as India – for example the biggest cinema group here (Vistarama) is opening cinemas in India and would like to be involved. Falcon Brookmotor is now an Indian company etc.

So if you could come up with something that looks professional, and attracts the interest of sponsors and spectators that would be great – the event will also attract the interest of the media, and will be followed by our Blossom Gala, which is also something for which we will need a flyer.

The tournament's first game is at 11.am
Refreshments will be available
Sponsors will also be showcasing their products
Kids welcome
Address - Quenvaro Sporting Club, Santa Clara de Ixhuatlan, Cerros Altos, Mexico

Target Market(s)

The flyer aims to attract the interest of spectators (families) from the various communities involved (British, Australian, Indian and Mexican) for a high end event that we will look to repeat every year.
We also want to attract the interest of sponsors of high end brands who want to be associated with the event.

Industry/Entity Type

Club

Requirements
Must have
• Logo of Halberd Bat League

```html
<!DOCTYPE html>
<html lang="en">
<head>
<meta charset="utf-8">
<title>Envoys Shield – Cricket Flyer</title>
<link rel="stylesheet" href="https://fonts.googleapis.com/css2?family=Nunito:wght@900&family=Mulish:wght@400;600;700;800&display=swap">
<style>
  :root {
    --red: #c8202f;
    --red-dark: #8e1420;
    --pink: #e9a29a;
    --wall: #e6e6e6;
    --wall-light: #f7f7f7;
    --wall-dark: #bdbdbd;
    --floor: #dcdcdc;
    --floor-line: #c3c3c3;
    --ink: #3f3f3f;
    --ink-soft: #555555;
    --white: #ffffff;
  }
  * { margin: 0; padding: 0; box-sizing: border-box; }
  html, body { width: 851px; height: 1200px; overflow: hidden; background: var(--white); }
  .flyer {
    position: relative;
    width: 851px;
    height: 1200px;
    overflow: hidden;
    font-family: "Mulish", Arial, sans-serif;
    color: var(--ink);
    background:
      radial-gradient(ellipse 70% 55% at 50% 38%, var(--wall-light) 0%, var(--wall) 55%, var(--wall-dark) 100%);
  }
  .floor {
    position: absolute;
    left: 0; right: 0; top: 918px; bottom: 0;
    background:
      linear-gradient(180deg, rgba(0,0,0,0.10) 0%, rgba(0,0,0,0) 18%),
      repeating-linear-gradient(90deg, var(--floor) 0 118px, var(--floor-line) 118px 120px),
      var(--floor);
  }
  .floor::before {
    content: "";
    position: absolute; inset: 0;
    background: linear-gradient(90deg, rgba(255,255,255,0.35), rgba(255,255,255,0) 40%, rgba(255,255,255,0.35));
  }
  .splash-art {
    position: absolute;
    left: 0; top: 0;
    width: 851px; height: 560px;
    background:
      radial-gradient(ellipse 38% 30% at 48% 38%, rgba(200,32,47,0.85) 0%, rgba(200,32,47,0.55) 45%, rgba(233,162,154,0.35) 75%, rgba(233,162,154,0) 100%),
      radial-gradient(ellipse 30% 22% at 80% 20%, rgba(233,162,154,0.55) 0%, rgba(233,162,154,0) 100%),
      radial-gradient(ellipse 25% 25% at 15% 55%, rgba(200,32,47,0.45) 0%, rgba(200,32,47,0) 100%);
  }
  .title {
    position: absolute;
    left: 40px; top: 190px;
    width: 780px;
    text-align: center;
    font-family: "Nunito", Arial, sans-serif;
    font-weight: 900;
    font-size: 76px;
    line-height: 1;
    color: var(--white);
    -webkit-text-stroke: 3px var(--red-dark);
    paint-order: stroke fill;
    text-shadow: 4px 5px 0 var(--red-dark);
    transform: rotate(-13deg);
  }
  .date {
    position: absolute;
    left: 225px; top: 365px;
    font-weight: 800;
    font-size: 41px;
    color: var(--ink-soft);
    transform: rotate(-10deg);
    transform-origin: left center;
    white-space: nowrap;
  }
  .date-day { color: var(--red); }
  .venue-time {
    position: absolute;
    left: 360px; top: 425px;
    font-weight: 800;
    font-size: 26px;
    color: var(--ink-soft);
    transform: rotate(-10deg);
    transform-origin: left center;
    white-space: nowrap;
  }
  .teams {
    position: absolute;
    right: 40px; top: 595px;
    width: 520px;
    text-align: right;
    font-weight: 800;
    font-size: 24px;
    line-height: 1.38;
    color: var(--ink);
  }
  .extras {
    position: absolute;
    left: 62px; top: 792px;
    font-size: 17px;
    line-height: 1.7;
    color: var(--ink);
  }
  .tagline {
    position: absolute;
    left: 64px; top: 866px;
    font-weight: 800;
    font-size: 38px;
    color: var(--red);
  }
  .organizer {
    position: absolute;
    left: 52px; top: 978px;
    width: 240px;
  }
  .organizer-label {
    font-size: 21px;
    color: var(--ink);
    margin-bottom: 16px;
  }
  .organizer-name {
    display: flex;
    align-items: center;
    gap: 12px;
    font-weight: 800;
    font-size: 22px;
    line-height: 1.15;
    color: var(--red);
  }
  .organizer-dot {
    flex: 0 0 auto;
    width: 46px; height: 46px;
    border-radius: 50%;
    background: var(--red);
  }
  .address {
    position: absolute;
    right: 28px; top: 978px;
    text-align: right;
    color: var(--ink);
  }
  .address-label { font-size: 21px; margin-bottom: 26px; }
  .address-lines { font-size: 23px; line-height: 1.28; }
</style>
</head>
<body>
  <main class="flyer">
    <div class="floor"></div>
    <div class="splash-art" role="img" aria-label="Red and pink paint splash with cheering crowd silhouettes, trophies, flags and a target"></div>

    <h1 class="title">Envoys Shield</h1>
    <p class="date">Saturday <span class="date-day">22 March 2014</span></p>
    <p class="venue-time">11am Quenvaro Sporting Club</p>

    <p class="teams">Great Britain, Australia, India and Mexico teams compete in the 20/20 game of the cricket</p>

    <p class="extras">Refreshments<br>Products showcase</p>
    <p class="tagline">Fun For All Family!</p>

    <section class="organizer">
      <p class="organizer-label">Organized by:</p>
      <p class="organizer-name"><span class="organizer-dot"></span>Halberd Bat League</p>
    </section>

    <section class="address">
      <p class="address-label">Address:</p>
      <p class="address-lines">Quenvaro Sporting<br>Club, Santa Clara de<br>Ixhuatlan, Cerros<br>Altos, Mexico</p>
    </section>
  </main>
</body>
</html>
```